Brochure for Residential Care Home

www.brelwickcare.co.uk
Simple fresh design required for this beautiful care home in Oxted, Surrey.
Copy and photos provided. This will be a collaboration between us and my client who will have the final say. For the sake of transparency they can sometimes be a bit slow.

Link for Photos - https://www.filetrove.example/sh/qx8tpbwz4471hav/BBD1JqLM5RbQaT8spJfw-gHeLb?dl=0

Brochure to span over 4 pages, with the location on the back.
Please highlight 20 years in some way and be creative but sensitive to the subject manner.

Once the design has been finalised a second brochure for their sister home is also required. Mostly same text and a few photo changes.

```html
<!DOCTYPE html>
<html lang="en">
<head>
<meta charset="utf-8">
<title>Hollins Lodge – Brochure Spread</title>
<link rel="stylesheet" href="https://fonts.googleapis.com/css2?family=Open+Sans:ital,wght@0,400;0,700;1,400;1,600&family=Russo+One&display=swap">
<style>
  :root {
    --backdrop: #cfe6ea;
    --paper: #f7f6fb;
    --ink: #5a4e86;
    --accent: #d8336f;
    --heading-black: #111014;
    --band: #3a2f8e;
    --photo-warm-1: #c9a27a;
    --photo-warm-2: #6e4f3a;
    --photo-cool-1: #d9d3c6;
    --photo-cool-2: #8a7a66;
  }
  * { box-sizing: border-box; margin: 0; padding: 0; }
  html, body { width: 1200px; height: 789px; overflow: hidden; }
  body {
    background: var(--backdrop);
    font-family: "Open Sans", Arial, sans-serif;
    position: relative;
  }
  .spread {
    position: absolute;
    left: 90px; top: 40px;
    width: 1020px; height: 709px;
    display: flex;
  }
  .page {
    position: relative;
    width: 510px; height: 100%;
    background: var(--paper);
    overflow: hidden;
  }
  .page--left { border-right: 1px solid #e2e0ec; }
  .page-band {
    position: absolute; left: 0; right: 0; bottom: 0;
    height: 12px; background: var(--band);
  }
  .copy {
    position: absolute;
    font-style: italic;
    font-size: 12px;
    line-height: 1.5;
    color: var(--ink);
  }
  .copy p + p { margin-top: 10px; }
  .hl { color: var(--accent); font-weight: 600; }

  .photo {
    position: absolute;
    box-shadow: 0 1px 3px rgba(0,0,0,.25);
  }
  .photo--lounge { background: linear-gradient(135deg, var(--photo-cool-1), var(--photo-cool-2)); }
  .photo--dining { background: linear-gradient(160deg, var(--photo-warm-1), var(--photo-warm-2)); }
  .photo--bedroom { background: linear-gradient(120deg, #e3d8c2, #9c8468); }
  .photo--salon { background: linear-gradient(140deg, #d8cdbd, #5d4a3c); }

  /* Left page main title */
  .title-facilities {
    position: absolute; left: 40px; top: 40px;
    background: var(--heading-black);
    color: #fff;
    font-family: "Russo One", "Arial Black", sans-serif;
    font-size: 24px;
    letter-spacing: 3px;
    padding: 4px 16px 3px;
    transform: rotate(-2deg);
    border-bottom: 5px solid var(--accent);
    text-shadow: 2px 2px 0 var(--accent);
  }

  /* Right page section tags */
  .tag {
    position: absolute;
    background: var(--accent);
    color: #fff;
    font-family: "Russo One", "Arial Black", sans-serif;
    font-size: 15px;
    letter-spacing: 1px;
    padding: 3px 14px;
  }
  .tag::before {
    content: "";
    position: absolute;
    left: -14px; top: -6px;
    width: 40px; height: 8px;
    background: var(--heading-black);
  }
</style>
</head>
<body>
<main class="spread">
  <section class="page page--left">
    <h1 class="title-facilities">FACILITIES</h1>

    <div class="copy" style="left:40px; top:92px; width:270px;">
      <p>Hollins Lodge has two <span class="hl">large reception rooms</span> and a bright sun room which leads to the impressive gardens and patio area. As you would expect, they are furnished with comfortable arm chairs, TVs and a piano.</p>
    </div>
    <div class="photo photo--lounge" role="img" aria-label="Photo of a reception room with armchairs and large windows" style="left:325px; top:82px; width:150px; height:105px;"></div>

    <div class="photo photo--dining" role="img" aria-label="Photo of the dining room with laid tables" style="left:40px; top:200px; width:200px; height:88px;"></div>
    <div class="copy" style="left:255px; top:200px; width:220px;">
      <p>The <span class="hl">elegant dining room</span> has recently undergone a full refurbishment and serves freshly prepared meals each day. A varied menu is planned with our guests, and special diets are always catered for.</p>
    </div>

    <div class="copy" style="left:40px; top:310px; width:215px;">
      <p>All 41 of our <span class="hl">bedrooms</span> have their own unique features, many with en-suite facilities, all with television points and nurse call systems. Guests are encouraged to bring small items of furniture and personal keepsakes so that their room truly feels like home. We are proud to keep every room warm, clean and welcoming.</p>
    </div>
    <div class="photo photo--bedroom" role="img" aria-label="Photo of a guest bedroom" style="left:275px; top:330px; width:190px; height:95px;"></div>

    <div class="photo photo--salon" role="img" aria-label="Photo of the hair salon" style="left:40px; top:500px; width:150px; height:80px;"></div>
    <div class="copy" style="left:205px; top:515px; width:270px;">
      <p>Hollins Lodge features its own <span class="hl">hair salon</span> for our guests to relax in once a week and 3 monthly visits from a Chiropodist.</p>
    </div>

    <div class="copy" style="left:40px; top:605px; width:435px;">
      <p>We will assist in facilitating <span class="hl">dentist and doctor appointments</span> as and when required.<br>Guest <span class="hl">laundry</span> is undertaken on the premises.</p>
    </div>
    <div class="page-band"></div>
  </section>

  <section class="page page--right">
    <h2 class="tag" style="left:55px; top:100px;">HEALTHCARE</h2>
    <div class="copy" style="left:40px; top:138px; width:430px;">
      <p>Hollins Lodge is not a nursing home, our staff are well trained and experienced in caring and supporting guests with their daily needs. Each guest has a personal care plan, agreed with their family and reviewed regularly. Local doctors visit weekly and district nurses attend whenever required.</p>
    </div>

    <h2 class="tag" style="left:55px; top:245px;">RESIDENCY PROCEDURE</h2>
    <div class="copy" style="left:40px; top:283px; width:430px;">
      <p>The first step in deciding whether Hollins Lodge is the right home for your loved one is to arrange a visit. Our manager will show you around, answer your questions and explain how we work. Following this, an assessment will be carried out to make sure we can fully meet their needs. Once a room has been agreed, we will work with the family to plan a settled and gentle move, and we welcome personal belongings to help the new room feel familiar from the very first day.</p>
      <p>Visitors are always most welcome, however we ask guests' loved ones to respect mealtimes.</p>
    </div>

    <h2 class="tag" style="left:55px; top:490px;">FEES</h2>
    <div class="copy" style="left:40px; top:528px; width:430px;">
      <p>A full list of services and associated costs are available upon application and will depend on the room chosen. Fees are payable monthly in advance.</p>
      <p>Hollins Lodge is fully insured; however, we cannot accept responsibility for valuables unless they are handed to the office for safe keeping.</p>
    </div>
    <div class="page-band"></div>
  </section>
</main>
</body>
</html>
```